Real estate company needs a card that makes you say WOW!

We need an awesome business card for our real estate company, Stonebrook Realty Partners of Chicago, that will stand out from the crowd. We specialize in buying and selling real estate, property management, and real estate investments (Flips & Rentals). On the business card, I need the following:

- Our logo
- Services
- My name & contact info (Derek Ollanby, 630-517-2946, Derek@StonebrookRPC.com)
- My title (Director of Acquisitions)
- StonebrookRPC.com

I attached an EPS file of our logo. Let me know if you have any questions. Thank you in advance!

```html
<!DOCTYPE html>
<html lang="en">
<head>
<meta charset="utf-8">
<title>Stonebrook Realty Partners of Chicago – Business Card</title>
<link href="https://fonts.googleapis.com/css2?family=Cinzel:wght@400;600&family=Open+Sans:wght@400;600&display=swap" rel="stylesheet">
<style>
  :root {
    --page-bg: #e9e7e4;
    --sky-light: #3fb6ea;
    --sky-mid: #1f8fd3;
    --sky-deep: #0b5fa8;
    --night: #0b0e12;
    --night-edge: #1b2129;
    --accent-blue: #2a9fe0;
    --soft-white: #f3f7fb;
    --muted-grey: #c9ced4;
    --shadow-grey: #2a3038;
  }
  * { box-sizing: border-box; margin: 0; padding: 0; }
  html, body {
    width: 1200px; height: 800px; overflow: hidden;
    background: var(--page-bg);
  }
  .canvas {
    position: relative; width: 1200px; height: 800px;
    display: flex; align-items: center; justify-content: center; gap: 50px;
  }
  .card {
    position: relative; width: 525px; height: 300px; overflow: hidden;
    border-radius: 4px;
    box-shadow: 0 10px 28px rgba(0,0,0,.25);
  }

  /* Front card */
  .card--front {
    background: linear-gradient(180deg, var(--sky-light) 0%, var(--sky-mid) 60%, var(--sky-deep) 100%);
    color: var(--soft-white);
  }
  .front__arc { position: absolute; left: 0; bottom: 0; width: 525px; height: 300px; }
  .front__skyline {
    position: absolute; left: 0; right: 0; bottom: 0; height: 150px;
    background: linear-gradient(180deg, rgba(14,92,160,0) 0%, rgba(14,92,160,.55) 45%, rgba(10,74,135,.85) 100%);
  }
  .front__brand {
    position: absolute; top: 40px; left: 0; right: 0; text-align: center;
    font-family: "Cinzel", serif; font-weight: 400; font-size: 30px;
    letter-spacing: 1px; line-height: 1.15;
  }
  .front__services {
    position: absolute; top: 135px; left: 0; right: 0; text-align: center;
    font-family: "Open Sans", sans-serif; font-size: 12.5px; line-height: 1.7;
  }

  /* Back card */
  .card--back {
    background: radial-gradient(ellipse at 80% 20%, var(--night-edge) 0%, var(--night) 70%);
    color: var(--muted-grey);
  }
  .back__skyline {
    position: absolute; left: 0; bottom: 0; width: 230px; height: 210px;
    background: linear-gradient(180deg, rgba(42,48,56,0) 0%, rgba(42,48,56,.7) 40%, var(--shadow-grey) 100%);
  }
  .back__logo {
    position: absolute; top: 28px; left: 36px; display: flex; align-items: center; gap: 10px;
  }
  .back__logo-mark { width: 14px; height: 14px; background: var(--accent-blue); }
  .back__logo-name {
    font-family: "Cinzel", serif; font-weight: 400; font-size: 18px;
    color: var(--accent-blue); letter-spacing: .5px;
  }
  .back__person { position: absolute; right: 32px; top: 120px; text-align: right; }
  .person__name {
    font-family: "Cinzel", serif; font-weight: 600; font-size: 21px;
    color: var(--accent-blue); letter-spacing: 1px;
  }
  .person__title { font-family: "Open Sans", sans-serif; font-size: 12.5px; margin-top: 2px; }
  .back__contacts {
    position: absolute; right: 32px; top: 192px; list-style: none;
    font-family: "Open Sans", sans-serif; font-size: 13px; color: var(--soft-white);
  }
  .contact { display: flex; align-items: center; justify-content: flex-end; gap: 8px; height: 22px; }
  .contact__icon { width: 14px; height: 14px; }
</style>
</head>
<body>
<main class="canvas">

  <section class="card card--front" aria-label="Card front">
    <div class="front__skyline" role="img" aria-label="Chicago skyline silhouette"></div>
    <svg class="front__arc" viewBox="0 0 525 300" aria-hidden="true">
      <path d="M0 250 Q262 200 525 250" fill="none" stroke="rgba(255,255,255,.35)" stroke-width="3"/>
      <path d="M0 262 Q262 214 525 262" fill="none" stroke="rgba(11,80,150,.6)" stroke-width="6"/>
    </svg>
    <h1 class="front__brand">Stonebrook Realty Partners<br>of Chicago</h1>
    <p class="front__services">
      Buying and Selling Real Estate<br>
      Property Management | Real Estate Investments (Flips &amp; Rentals)
    </p>
  </section>

  <section class="card card--back" aria-label="Card back">
    <div class="back__skyline" role="img" aria-label="Faint Chicago skyline silhouette"></div>
    <div class="back__logo">
      <span class="back__logo-mark" aria-hidden="true"></span>
      <span class="back__logo-name">Stonebrook Realty Partners of Chicago</span>
    </div>
    <div class="back__person">
      <h2 class="person__name">Derek Ollanby</h2>
      <p class="person__title">Director of Acquisitions</p>
    </div>
    <ul class="back__contacts">
      <li class="contact">630-517-2946
        <svg class="contact__icon" viewBox="0 0 14 14" aria-hidden="true"><rect width="14" height="14" rx="2" fill="#1d5f8c"/><rect x="4.5" y="2.5" width="5" height="9" rx="1" fill="none" stroke="#cfe8f8" stroke-width="1.2"/></svg>
      </li>
      <li class="contact">Derek@StonebrookRPC.com
        <svg class="contact__icon" viewBox="0 0 14 14" aria-hidden="true"><rect width="14" height="14" rx="2" fill="#1d5f8c"/><rect x="2.5" y="4" width="9" height="6" fill="none" stroke="#cfe8f8" stroke-width="1.2"/><path d="M2.5 4 L7 7.5 L11.5 4" fill="none" stroke="#cfe8f8" stroke-width="1.2"/></svg>
      </li>
      <li class="contact">StonebrookRPC.com
        <svg class="contact__icon" viewBox="0 0 14 14" aria-hidden="true"><rect width="14" height="14" rx="2" fill="#1d5f8c"/><circle cx="7" cy="7" r="4.2" fill="none" stroke="#cfe8f8" stroke-width="1.1"/><path d="M2.8 7 H11.2 M7 2.8 Q4.5 7 7 11.2 M7 2.8 Q9.5 7 7 11.2" fill="none" stroke="#cfe8f8" stroke-width="1"/></svg>
      </li>
    </ul>
  </section>

</main>
</body>
</html>
```